Gratefl Moments/Coral Friday

Create a double sided postcard which will be distributed to 60,000 destinations, suitable for printing on re-cycled card.

Promotional offer ends Sunday August 31st 2014

It is Winter in Perth Western Australia, colours need to be bright and a reminder of summer. The card needs to be fun with a Mediterranean Spanish type feel
web site www.kelvport.com.au

```html
<!DOCTYPE html>
<html lang="en">
<head>
<meta charset="utf-8">
<title>Kelvport Bay – Coral Friday Postcard</title>
<link rel="stylesheet" href="https://fonts.googleapis.com/css2?family=Roboto:wght@300;400;700&family=Roboto+Condensed:wght@400&display=swap">
<style>
  :root {
    --bay-blue: #1b5fa8;
    --bay-blue-light: #3f86c8;
    --ink: #1d1d1b;
    --paper: #ffffff;
    --backdrop: #e9e7e3;
    --stamp: #1a1a1a;
    --rule: #2a2a2a;
  }
  * { box-sizing: border-box; margin: 0; padding: 0; }
  html, body { width: 764px; height: 1200px; overflow: hidden; }
  body {
    background: var(--backdrop);
    font-family: "Roboto", Arial, sans-serif;
    color: var(--ink);
    position: relative;
  }
  .card {
    position: absolute;
    left: 39px;
    width: 685px;
    background: var(--paper);
    box-shadow: 0 2px 6px rgba(0,0,0,.18);
    overflow: hidden;
  }

  /* ---------- Front ---------- */
  .front { top: 45px; height: 533px; }
  .front-title {
    position: absolute; left: 15px; top: 16px;
    font-weight: 300; font-size: 26px; line-height: 32px;
  }
  .front-intro {
    position: absolute; right: 18px; top: 22px; width: 300px;
    text-align: right;
    font-family: "Roboto Condensed", Arial, sans-serif;
    font-size: 13.5px; line-height: 17px;
  }
  .front-art { position: absolute; left: 0; top: 80px; }
  .plate-name {
    position: absolute; left: 15px; top: 417px;
    font-weight: 300; font-size: 17px;
  }
  .plate-price {
    position: absolute; left: 13px; top: 436px;
    font-weight: 700; font-size: 36px; letter-spacing: -0.5px;
  }
  .plate-price .unit { font-weight: 300; }
  .plate-items {
    position: absolute; left: 15px; top: 483px;
    font-size: 12px;
  }
  .brand-box {
    position: absolute;
    background: var(--bay-blue);
    color: var(--paper);
    display: flex; align-items: center; justify-content: center;
    font-weight: 400; letter-spacing: 2px;
  }
  .front .brand-box { left: 358px; top: 437px; width: 131px; height: 64px; font-size: 13px; }
  .front-address {
    position: absolute; left: 502px; top: 450px;
    font-size: 11px; line-height: 15px;
  }
  .front-band {
    position: absolute; left: 0; bottom: 0; width: 100%; height: 22px;
    background: var(--bay-blue);
    color: var(--paper);
    font-weight: 300; font-size: 15px;
    text-align: center; line-height: 22px;
  }

  /* ---------- Back ---------- */
  .back { top: 622px; height: 528px; }
  .lunch-panel {
    position: absolute; left: 0; top: 0; width: 514px; height: 170px;
    background: var(--bay-blue);
    color: var(--paper);
    text-align: center;
  }
  .lunch-headline { margin-top: 14px; font-weight: 300; font-size: 25px; line-height: 32px; }
  .lunch-price { margin-top: 4px; font-weight: 700; font-size: 32px; }
  .lunch-hours { margin-top: 8px; font-weight: 300; font-size: 15px; }
  .stamp-box {
    position: absolute; left: 523px; top: 21px; width: 135px; height: 139px;
    background: var(--stamp);
  }
  .menu {
    position: absolute; left: 0; top: 176px; width: 344px;
    text-align: center;
    font-family: "Roboto Condensed", Arial, sans-serif;
    font-size: 11.5px; line-height: 13.7px;
  }
  .divider-v { position: absolute; left: 344px; top: 171px; width: 1px; height: 287px; background: var(--rule); }
  .divider-h { position: absolute; left: 0; top: 458px; width: 100%; height: 1px; background: var(--rule); }
  .address-to {
    position: absolute; left: 409px; top: 252px; font-size: 11px;
  }
  .address-line { position: absolute; left: 431px; width: 186px; height: 1px; background: #555; }
  .back .brand-box { left: 17px; top: 463px; width: 102px; height: 50px; font-size: 10px; }
  .back-contact {
    position: absolute; left: 210px; top: 468px; text-align: left;
  }
  .back-contact .bookings { font-weight: 300; font-size: 16px; }
  .back-contact .address { font-size: 11px; margin-top: 2px; }
</style>
</head>
<body>

<section class="card front">
  <h1 class="front-title">Celebrate<br>Coral Friday’s</h1>
  <p class="front-intro">Celebrate Sunday’s on Perth’s most beautiful bay with a selection of magnificent Western Australian seafood, from Shark Bay.</p>

  <svg class="front-art" width="685" height="330" viewBox="0 0 685 330">
    <defs>
      <linearGradient id="dishTones" x1="0" y1="0" x2="1" y2="0.4">
        <stop offset="0" stop-color="#7a3a2a"/>
        <stop offset="0.35" stop-color="#c2452c"/>
        <stop offset="0.7" stop-color="#8c3a2c"/>
        <stop offset="1" stop-color="#5a6b88"/>
      </linearGradient>
    </defs>
    <path d="M0 30 C200 -5 480 0 685 35 L685 320 C480 300 200 310 0 325 Z" fill="var(--bay-blue)"/>
    <path d="M0 42 C220 30 470 40 685 80 L685 305 C480 282 220 292 0 310 Z" fill="var(--bay-blue-light)"/>
    <path role="img" aria-label="Photo of a whole grilled red fish topped with ginger strips on a blue and white plate"
          d="M0 52 C220 50 470 62 685 98 L685 292 C480 270 220 280 0 298 Z" fill="url(#dishTones)"/>
  </svg>

  <p class="plate-name">Coral Friday Plate</p>
  <p class="plate-price">$38.00<span class="unit">pp</span></p>
  <p class="plate-items">Grilled Scampi, Prawns, Cuttlefish, Pink Snapper and Scallops</p>

  <div class="brand-box">KELVPORT</div>
  <p class="front-address">Kelvport Bay Restaurant and<br>Function Centre<br>18 Shoreline Drive Crawley 600</p>

  <div class="front-band">Bookings w: www.kelvport.com.au p 9555-0142</div>
</section>

<section class="card back">
  <div class="lunch-panel">
    <p class="lunch-headline">Gratefl Moments with Lunch overlooking<br>Perth’s most beautiful Bay</p>
    <p class="lunch-price">$48.00 per person</p>
    <p class="lunch-hours">(Available Monday to Friday 11am until 3pm)</p>
  </div>
  <div class="stamp-box" aria-hidden="true"></div>

  <div class="menu">
    <p>Select one dish from each course with your choice of either a glass<br>of Colle Verde Soave 2011 or Villa Serena ValpolicellaClassico 2011</p>
    <p>Freshly baked Italian style crusty bread,</p>
    <p>Entrée</p>
    <p>Passionfruit and citrus cured Tasmanian salmon</p>
    <p>or</p>
    <p>Pork belly, marinated, horseradish coleslaw</p>
    <p>or</p>
    <p>Welsh rarebit, sautéed mushrooms, hot English mustard mayo</p>
    <p>or</p>
    <p>Fried squid, tubes, cannellini pure, green chilli sauce</p>
    <p>Main</p>
    <p>Pink snapper fillet, grilled, xo sauce, kim chi</p>
    <p>or</p>
    <p>Wagyu rump, served with cauliflower puree, broad beans</p>
    <p>or</p>
    <p>Soft polenta, grilled haloumi, crusted eggplant, red pepper coulis</p>
    <p>or</p>
    <p>Confit duck leg caramelised red onion, grilled manchego stuffed fig</p>
  </div>

  <div class="divider-v"></div>
  <div class="divider-h"></div>

  <p class="address-to">To,</p>
  <div class="address-line" style="top:262px"></div>
  <div class="address-line" style="top:295px"></div>
  <div class="address-line" style="top:327px"></div>
  <div class="address-line" style="top:359px"></div>

  <div class="brand-box">KELVPORT</div>
  <div class="back-contact">
    <p class="bookings">Bookings w: www.kelvport.com.au p 9555-0142</p>
    <p class="address">Kelvport Bay Restaurant and Function Centre 18 Shoreline Drive Crawley 6009</p>
  </div>
</section>

</body>
</html>
```